Roofing Company Now Hiring and Call Now Facebook Ads

Trying to hire new sales reps in our Alabama market to add to our growing team. This is a great opportunity for any one looking for a career change or looking to add time back to the time they get to spend at home with their families. This is a chance to build a career in one of the fastest growing industries in the country and build financial freedom and a solid future for your family while easily making 6 figures yearly. Sales reps get to set their own schedule, take vacations when they want, and could even choose if they wanted to work in the summer or the winter seasons if they dont like the heat/cold environment. Sales reps are commission based with bonus/incentives for completing task and assignments weekly.

"Let's Talk About Your Roof!" Schedule a free Roof Inspection today!

Needing facebook ads for hiring and a few ads templates for daily post regarding roof inspections and roof replacements, if they are editable it would be easier for me to manage a few templates. This project needs to have a swag/cleanish look that attracts the younger group of people but still make the older group of customer think, man these guys have some solid looking things going on and looks like a well managed and built company. We also target the upper scale areas when seeking customers.

Lets see what yall got! lets Gooo!

Target Market(s)

Property owners, sales reps, homeowners, property managers, job seekers

Industry/Entity Type

Roofing Contractor Storm Restoration Contractor, Construction Contractor

Font styles to use
Sans Serif

Colors
EB3D1F
EC4F4E
F09395
F8D3D4
FCEDEE

Requirements
Must have
• Clean modern professional look with visible red and black colors, we like white too.
Nice to have
• red, black, white, popping eye catching colors.
Should not have
• wrong color red, red is more of a kelvard herons red, please stay away from the pinkish red.

```html
<!DOCTYPE html>
<html lang="en">
<head>
<meta charset="UTF-8">
<title>Ironcrest Roofing – Free Roof Inspection</title>
<link rel="stylesheet" href="https://fonts.googleapis.com/css2?family=Bebas+Neue&family=Poppins:wght@300;400;600;700;800&display=swap">
<style>
  :root {
    --red: #d20a1a;
    --black: #0e0b0b;
    --white: #ffffff;
    --page: #f2f7f4;
    --ink-light: #f4f7f5;
  }
  * { margin: 0; padding: 0; box-sizing: border-box; }
  html, body { width: 1200px; height: 1200px; overflow: hidden; background: var(--page); }
  body { position: relative; font-family: "Poppins", sans-serif; color: var(--black); }

  .ad-card { position: absolute; left: 94px; top: 94px; width: 1011px; height: 1011px; background: var(--white); overflow: hidden; }
  .ad-card > * { position: absolute; }

  .brand { left: 50px; top: 108px; width: 300px; text-align: center; font-weight: 600; color: var(--black); }
  .brand-mark { width: 22px; height: 22px; background: var(--red); margin: 0 auto 36px; }
  .brand-name { font-size: 46px; line-height: 1; letter-spacing: 1px; }
  .brand-sub { font-size: 16px; line-height: 1; letter-spacing: 12px; margin-top: 10px; padding-left: 12px; }

  .tagline-band { left: 409px; top: 50px; width: 556px; height: 47px; background: var(--red); color: var(--white); font-family: "Bebas Neue", sans-serif; font-size: 27px; letter-spacing: 1.3px; line-height: 47px; text-align: center; }
  .photo-commercial { left: 409px; top: 97px; width: 556px; height: 290px; background: linear-gradient(160deg, #c9ccd0 0%, #a9aeb3 45%, #7d8a73 100%); }

  .accent-red-left { left: 41px; top: 274px; width: 50px; height: 160px; background: var(--red); }
  .headline-block { left: 41px; top: 542px; width: 428px; height: 328px; background: var(--black); }
  .accent-red-corner-v { left: 935px; top: 506px; width: 22px; height: 159px; background: var(--red); }
  .accent-red-corner-h { left: 749px; top: 647px; width: 208px; height: 18px; background: var(--red); }
  .photo-home { left: 90px; top: 274px; width: 845px; height: 373px; background: linear-gradient(180deg, #8fb6dc 0%, #c9dcec 35%, #7891ab 60%, #4f6a45 100%); }

  .headline { left: 67px; top: 668px; width: 400px; height: 180px; color: var(--ink-light); font-weight: 400; }
  .headline > span { position: absolute; left: 0; line-height: 1; white-space: nowrap; }
  .headline-lead { top: 0; font-weight: 300; font-size: 58px; letter-spacing: 16px; }
  .headline-main { top: 57px; font-weight: 700; font-size: 60px; letter-spacing: -1px; }
  .headline-accent { top: 111px; font-weight: 800; font-size: 60px; letter-spacing: -1px; color: var(--red); }

  .services { left: 66px; top: 885px; display: grid; grid-template-columns: 258px auto; row-gap: 10px; list-style: none; font-size: 20px; font-weight: 400; }
  .services li { display: flex; align-items: center; gap: 6px; line-height: 24px; }
  .services svg { width: 16px; height: 16px; flex: none; }

  .cta { left: 520px; top: 684px; width: 420px; height: 135px; }
  .cta > span { position: absolute; left: 0; line-height: 1; white-space: nowrap; }
  .cta-lead { top: 0; font-weight: 700; font-size: 29px; letter-spacing: 6px; }
  .cta-offer { top: 34px; font-family: "Bebas Neue", sans-serif; font-size: 57px; color: var(--red); }
  .cta-time { top: 82px; font-weight: 800; font-size: 58px; }
  .cta-rule { left: 524px; top: 829px; width: 406px; height: 3px; background: var(--red); border-radius: 2px; }

  .phone { left: 525px; top: 850px; display: flex; align-items: center; gap: 10px; }
  .phone-icon { width: 39px; height: 39px; border-radius: 50%; background: var(--black); display: flex; align-items: center; justify-content: center; }
  .phone-number { font-weight: 600; font-size: 40px; color: var(--red); line-height: 1; letter-spacing: -0.5px; }

  .contacts { left: 499px; top: 931px; display: flex; align-items: center; gap: 9px; font-size: 17px; }
  .contacts svg { width: 14px; height: 14px; }
  .contacts .divider { width: 3px; height: 15px; background: var(--red); margin: 0 14px; }

  .footer-bar { left: 667px; top: 970px; width: 344px; height: 41px; background: var(--black); border-top-left-radius: 8px; }
</style>
</head>
<body>
<main class="ad-card">
  <div class="brand">
    <div class="brand-mark"></div>
    <div class="brand-name">IRONCREST</div>
    <div class="brand-sub">ROOFING</div>
  </div>

  <div class="tagline-band">Quality Roofing Meets Perfect Customer Service</div>
  <div class="photo-commercial" role="img" aria-label="Aerial view of large commercial buildings with white flat roofs and trees"></div>

  <div class="accent-red-left"></div>
  <div class="headline-block"></div>
  <div class="accent-red-corner-v"></div>
  <div class="accent-red-corner-h"></div>
  <div class="photo-home" role="img" aria-label="Blue two-storey house with dark shingle roof, white porch and trees under a cloudy sky"></div>

  <h1 class="headline">
    <span class="headline-lead">LET'S</span>
    <span class="headline-main">TALK ABOUT</span>
    <span class="headline-accent">YOUR ROOF!</span>
  </h1>

  <ul class="services">
    <li><svg viewBox="0 0 16 16"><circle cx="8" cy="8" r="8" fill="#d20a1a"/><path d="M4.5 8.2l2.3 2.3 4.7-4.8" stroke="#fff" stroke-width="1.8" fill="none" stroke-linecap="round"/></svg>Residential Roofing</li>
    <li><svg viewBox="0 0 16 16"><circle cx="8" cy="8" r="8" fill="#d20a1a"/><path d="M4.5 8.2l2.3 2.3 4.7-4.8" stroke="#fff" stroke-width="1.8" fill="none" stroke-linecap="round"/></svg>Gutters</li>
    <li><svg viewBox="0 0 16 16"><circle cx="8" cy="8" r="8" fill="#d20a1a"/><path d="M4.5 8.2l2.3 2.3 4.7-4.8" stroke="#fff" stroke-width="1.8" fill="none" stroke-linecap="round"/></svg>Commercial Roofing</li>
    <li><svg viewBox="0 0 16 16"><circle cx="8" cy="8" r="8" fill="#d20a1a"/><path d="M4.5 8.2l2.3 2.3 4.7-4.8" stroke="#fff" stroke-width="1.8" fill="none" stroke-linecap="round"/></svg>Siding</li>
  </ul>

  <div class="cta">
    <span class="cta-lead">SCHEDULE A</span>
    <span class="cta-offer">FREE ROOF INSPECTION</span>
    <span class="cta-time">TODAY!</span>
  </div>
  <div class="cta-rule"></div>

  <div class="phone">
    <div class="phone-icon">
      <svg width="22" height="22" viewBox="0 0 24 24"><path fill="#fff" d="M6.6 10.8c1.4 2.8 3.8 5.1 6.6 6.6l2.2-2.2c.3-.3.7-.4 1-.2 1.1.4 2.3.6 3.6.6.6 0 1 .4 1 1V20c0 .6-.4 1-1 1C10.6 21 3 13.4 3 4c0-.6.4-1 1-1h3.5c.6 0 1 .4 1 1 0 1.3.2 2.5.6 3.6.1.3 0 .7-.2 1l-2.3 2.2z"/></svg>
    </div>
    <div class="phone-number">(555) 214-3098</div>
  </div>

  <div class="contacts">
    <svg viewBox="0 0 16 16"><rect x="1" y="3" width="14" height="10" rx="1" fill="#d20a1a"/><path d="M1.5 3.5L8 9l6.5-5.5" stroke="#fff" stroke-width="1.2" fill="none"/></svg>
    <span>hello@ironcrestga.com</span>
    <span class="divider"></span>
    <svg viewBox="0 0 16 16"><circle cx="8" cy="8" r="7" fill="none" stroke="#d20a1a" stroke-width="1.4"/><ellipse cx="8" cy="8" rx="3" ry="7" fill="none" stroke="#d20a1a" stroke-width="1.2"/><path d="M1 8h14M2.5 4.5h11M2.5 11.5h11" stroke="#d20a1a" stroke-width="1.1"/></svg>
    <span>www.ironcrestga.com</span>
  </div>

  <div class="footer-bar"></div>
</main>
</body>
</html>
```